Local Flower Farm Needs Business Card Design

I need business cards designed for a flower farm based in Eudora, Kansas.
Business Info:
We are a local cut flower farm located in Eudora, Kansas, founded by Darla Hoffstrom. What started as a passion for agriculture and search for more joy in daily life has blossomed into a small business dedicated to providing the community with beautiful, fresh, and sustainable flowers. We specialize in local, seasonal blooms, ensuring that every petal reflects the care and dedication we pour into our craft. Our mission is to deliver the highest quality flowers directly to our customers through local farmers markets and to florists who share our commitment to sustainability. Join us in celebrating the beauty of nature, one bloom at a time!
Contact Details:
Darla Hoffstrom
Owner
Phone 913-555-0147
Facebook: Lorabelle Quinn Blossoms
Instagram: @LorabelleQuinnBlossoms
Website: LorabelleQuinnBlossoms.example
Target Market(s)
Wholesale to Florists and Direct to Consumer via Farmers Market
Industry/Entity Type
Florist, Farm
Contact Information for Business Card
Name, Contact Info, Logo
Look and feel

```html
<!DOCTYPE html>
<html lang="en">
<head>
<meta charset="utf-8">
<title>Lorabelle Quinn Blossoms – Business Card</title>
<link rel="stylesheet" href="https://fonts.googleapis.com/css2?family=Libre+Caslon+Text:wght@400;700&family=Poppins:wght@400&display=swap">
<style>
  :root {
    --canvas-bg: #e6e6e4;
    --card-white: #ffffff;
    --brand-teal: #0d2a2f;
    --ink-light: #ffffff;
    --ring-line: #1c3a3f;
  }
  * { box-sizing: border-box; margin: 0; padding: 0; }
  html, body {
    width: 1200px; height: 874px; overflow: hidden;
    background: var(--canvas-bg);
  }
  .canvas {
    width: 1200px; height: 874px;
    display: flex; flex-direction: column;
    align-items: center; justify-content: center; gap: 40px;
  }
  .card {
    width: 620px; height: 354px;
    position: relative;
    box-shadow: 0 10px 28px rgba(0,0,0,0.18);
  }
  /* Front */
  .card-front {
    background: var(--card-white);
    display: flex; align-items: center; justify-content: center;
  }
  .brand-seal {
    width: 206px; height: 206px;
    border: 1.5px solid var(--ring-line);
    border-radius: 50%;
    display: flex; flex-direction: column;
    align-items: center; justify-content: center; gap: 6px;
    text-align: center;
  }
  .brand-name {
    font-family: "Libre Caslon Text", serif;
    font-weight: 400;
    color: var(--brand-teal);
    font-size: 19px;
    letter-spacing: 2.5px;
    line-height: 1.35;
    text-transform: uppercase;
  }
  /* Back */
  .card-back {
    background: var(--brand-teal);
    color: var(--ink-light);
  }
  .inner-frame {
    position: absolute; inset: 12px;
    border: 1.5px solid rgba(255,255,255,0.85);
    display: flex; flex-direction: column;
    align-items: center; justify-content: center;
    text-align: center;
    padding-top: 10px;
  }
  .person-name {
    font-family: "Libre Caslon Text", serif;
    font-weight: 700;
    font-size: 27px;
    letter-spacing: 0.3px;
  }
  .person-role {
    font-family: "Poppins", sans-serif;
    font-size: 12px;
    margin-top: 2px;
  }
  .floral-mark {
    width: 30px; height: 30px;
    margin: 8px 0 8px;
    border-radius: 50%;
    background: rgba(255,255,255,0.25);
  }
  .contact-list {
    font-family: "Poppins", sans-serif;
    font-size: 14.5px;
    line-height: 1.32;
    list-style: none;
  }
  .social-divider {
    display: flex; align-items: center; gap: 6px;
    margin: 8px 0 4px;
  }
  .social-divider .rule {
    width: 46px; height: 1px; background: var(--ink-light);
    position: relative;
  }
  .social-divider .rule::before {
    content: ""; position: absolute; top: -2px;
    width: 5px; height: 5px; border-radius: 50%;
    background: var(--ink-light);
  }
  .social-divider .rule-left::before { left: -3px; }
  .social-divider .rule-right::before { right: -3px; }
  .social-dot {
    width: 18px; height: 18px; border-radius: 50%;
    background: var(--ink-light);
  }
  .social-handle {
    font-family: "Poppins", sans-serif;
    font-size: 14.5px;
  }
</style>
</head>
<body>
<main class="canvas">
  <section class="card card-front" aria-label="Card front">
    <div class="brand-seal">
      <p class="brand-name">Lorabelle Quinn<br>Blossoms</p>
    </div>
  </section>

  <section class="card card-back" aria-label="Card back">
    <div class="inner-frame">
      <h1 class="person-name">Darla Hoffstrom</h1>
      <p class="person-role">Owner</p>
      <div class="floral-mark" role="img" aria-label="Small line-drawn flower ornament"></div>
      <ul class="contact-list">
        <li>913-555-0147</li>
        <li>info@LorabelleQuinnBlossoms.example</li>
        <li>www.LorabelleQuinnBlossoms.example</li>
      </ul>
      <div class="social-divider">
        <span class="rule rule-left"></span>
        <span class="social-dot"></span>
        <span class="rule rule-right"></span>
      </div>
      <p class="social-handle">@LorabelleQuinnBlossoms</p>
    </div>
  </section>
</main>
</body>
</html>
```